website re-design - the brisk loft

The Brisk Loft is an existing website that we built using a new zealand based online CMS tool which is quite flexible and accomodates custom designs. You can check it here: http://www.pagecrafter.co.nz/.

We have a logo already and the content on the website is OK.
The website can be found at www.thebriskloft.com.au

mainly the homepage, but if the design is easily adapted to the other pages then, we will commission the winner to update these pages also.
Updates

Hi there,  I am uploading an image to be used as the main image on the homepage design,  so all submissions have the same image.

Target Market(s)

property developers, architects, builders, home buyers

Industry/Entity Type

Shop

Requirements
Must have
• Must utilise the existing CMS or at least be compatible to upload
Nice to have
• a promotional banner that can be turned off and on and changed as required as we offer different promotions over time.

```html
<!DOCTYPE html>
<html lang="en">
<head>
<meta charset="utf-8">
<title>The Brisk Loft – Architectural Scale Models</title>
<link rel="stylesheet" href="https://fonts.googleapis.com/css2?family=Source+Sans+3:wght@400;600&display=swap">
<style>
  :root {
    --orange: #f08a1c;
    --orange-light: #f7b25a;
    --ink: #1c1c1c;
    --text: #222;
    --grey-line: #c9c9c9;
    --nav-top: #fafafa;
    --nav-bottom: #e4e4e4;
    --footer: #303030;
    --footer-text: #f2f2f2;
    --page: #ffffff;
  }
  * { box-sizing: border-box; margin: 0; padding: 0; }
  html, body {
    width: 1122px; height: 1200px; overflow: hidden;
    background: var(--page);
    font-family: "Source Sans 3", "Segoe UI", sans-serif;
    color: var(--text);
  }
  .page { position: relative; width: 1122px; height: 1200px; }

  .brand { position: absolute; left: 118px; top: 16px; display: flex; align-items: center; gap: 14px; }
  .brand-mark { width: 90px; height: 52px; background: var(--orange); }
  .brand-name { font-size: 27px; font-weight: 600; color: #333; letter-spacing: .5px; line-height: 1; }
  .brand-tag { font-size: 12px; color: var(--orange); letter-spacing: .6px; margin-top: 3px; font-weight: 600; }

  .search { position: absolute; left: 810px; top: 36px; width: 192px; height: 26px;
    border: 1px solid #bbb; border-radius: 3px; display: flex; }
  .search-field { flex: 1; font-size: 15px; color: #777; padding: 2px 8px; }
  .search-button { width: 34px; border-left: 1px solid #bbb; display: flex; align-items: center; justify-content: center;
    background: linear-gradient(#fff, #e7e7e7); }

  .main-nav { position: absolute; left: 118px; top: 80px; width: 886px; height: 44px; display: flex;
    border: 1px solid var(--grey-line); border-radius: 4px;
    background: linear-gradient(var(--nav-top), var(--nav-bottom)); overflow: hidden; }
  .main-nav a { display: flex; align-items: center; justify-content: center; font-size: 15px; color: #111;
    text-decoration: none; border-right: 1px solid var(--grey-line); }
  .main-nav a:last-child { border-right: 0; }
  .main-nav a.current { background: linear-gradient(var(--orange-light), var(--orange)); }

  .hero { position: absolute; left: 118px; top: 135px; width: 886px; height: 372px;
    background: linear-gradient(#7aa0cc 0%, #c8d6e6 45%, #c9cdd3 62%, #8f9a86 80%, #6f7a6a 100%); }
  .hero-dots { position: absolute; right: 40px; bottom: 12px; display: flex; gap: 5px; }
  .hero-dots span { width: 10px; height: 10px; border-radius: 50%; background: #fff; }
  .hero-dots span.active { background: var(--orange); }

  .feature { position: absolute; top: 518px; width: 279px; }
  .feature h2 { font-size: 19px; font-weight: 400; color: var(--ink); height: 25px; }
  .feature-photo { height: 137px; }
  .feature p { font-size: 14px; line-height: 16.5px; margin-top: 6px; padding-left: 3px; }
  .read-more { display: block; text-align: right; color: var(--orange); font-size: 14px; margin-top: 11px; text-decoration: none; }

  .section-title { font-size: 26px; font-weight: 400; color: var(--ink); }
  .welcome { position: absolute; left: 120px; top: 800px; width: 590px; }
  .welcome p { font-size: 15.5px; line-height: 19.5px; }
  .welcome-body { display: flex; gap: 16px; margin: 11px 0 10px -2px; }
  .welcome-photo { width: 276px; height: 166px; flex: none; background: linear-gradient(135deg, #c9c2b6, #8e8477 60%, #3c3a36); }
  .welcome-aside p { margin-top: 0; }
  .welcome-aside ul { margin-top: 12px; list-style: none; font-size: 15px; line-height: 19.5px; }
  .welcome-aside li { position: relative; padding-left: 10px; }
  .welcome-aside li::before { content: ""; position: absolute; left: 0; top: 7px; width: 6px; height: 6px; border-radius: 50%; background: var(--ink); }

  .gallery { position: absolute; left: 729px; top: 800px; width: 275px; }
  .gallery-item { display: flex; gap: 6px; margin-top: 7px; height: 93px; }
  .gallery-item:first-of-type { margin-top: 10px; }
  .gallery-thumb { width: 130px; flex: none; border: 2px solid #555; }
  .gallery-item h3 { font-size: 16px; font-weight: 400; color: var(--orange); line-height: 19px; }
  .gallery-item p { font-size: 11.5px; line-height: 13.5px; margin-top: 4px; }

  .site-footer { position: absolute; left: 0; top: 1156px; width: 1122px; height: 44px; background: var(--footer);
    color: var(--footer-text); font-size: 13px; line-height: 15px; }
  .site-footer .legal { position: absolute; left: 120px; top: 7px; }
  .social { position: absolute; left: 906px; top: 9px; display: flex; gap: 9px; }
  .social span { width: 27px; height: 27px; border-radius: 3px; background: #777; border: 1px solid #999; }
</style>
</head>
<body>
<div class="page">
  <header>
    <div class="brand">
      <div class="brand-mark"></div>
      <div>
        <div class="brand-name">THE BRISK LOFT</div>
        <div class="brand-tag">ARCHITECTURAL SCALE MODELS</div>
      </div>
    </div>
    <div class="search">
      <div class="search-field">Search</div>
      <div class="search-button">
        <svg width="18" height="18" viewBox="0 0 18 18"><circle cx="7" cy="7" r="5" fill="none" stroke="#333" stroke-width="2"/><line x1="10.5" y1="10.5" x2="16" y2="16" stroke="#333" stroke-width="2.5" stroke-linecap="round"/></svg>
      </div>
    </div>
    <nav class="main-nav">
      <a class="current" style="width:87px">Home</a>
      <a style="width:101px">Gallery</a>
      <a style="width:124px">Order Online</a>
      <a style="width:117px">Get a Quote</a>
      <a style="width:147px">3D Visualisation</a>
      <a style="width:108px">About Us</a>
      <a style="width:97px">Contact</a>
      <a style="flex:1">Sitemap</a>
    </nav>
  </header>

  <section class="hero" role="img" aria-label="Rendered modern office building with curved glass facade on a street corner">
    <div class="hero-dots"><span></span><span class="active"></span><span></span><span></span></div>
  </section>

  <section class="feature" style="left:118px">
    <h2>Planning</h2>
    <div class="feature-photo" role="img" aria-label="Team planning a project around a table" style="background:linear-gradient(135deg,#e9e9e7,#b7ada3 55%,#5b6470)"></div>
    <p>Lorem ipsum dolor sit amet, consectetur adipiscing elit. Nullam eu urna enim, sit amet venenatis arcu. Proin ultrices rutrum ante, sed cursus leo sollicitudin in. Integer hendrerit congue dui, at tincidunt.</p>
    <a class="read-more">read more...</a>
  </section>
  <section class="feature" style="left:423px">
    <h2>Analysis</h2>
    <div class="feature-photo" role="img" aria-label="Hands reviewing documents beside a laptop" style="background:linear-gradient(135deg,#2e3a4f,#a29a8a 55%,#d9d4c8)"></div>
    <p>Lorem ipsum dolor sit amet, consectetur adipiscing elit. Nullam eu urna enim, sit amet venenatis arcu. Proin ultrices rutrum ante, sed cursus leo sollicitudin in. Integer hendrerit congue dui, at tincidunt.</p>
    <a class="read-more">read more...</a>
  </section>
  <section class="feature" style="left:727px">
    <h2>Modeling</h2>
    <div class="feature-photo" role="img" aria-label="Scale model of high-rise apartment towers" style="background:linear-gradient(#e4e4e4,#cfd2d2 60%,#6f8a5e)"></div>
    <p>Lorem ipsum dolor sit amet, consectetur adipiscing elit. Nullam eu urna enim, sit amet venenatis arcu. Proin ultrices rutrum ante, sed cursus leo sollicitudin in. Integer hendrerit congue dui, at tincidunt.</p>
    <a class="read-more">read more...</a>
  </section>

  <section class="welcome">
    <h2 class="section-title">Welcome</h2>
    <p>Lorem ipsum dolor sit amet, consectetur adipiscing elit. Nullam eu urna enim, sit amet venenatis arcu. Proin ultrices rutrum ante, sed cursus leo sollicitudin in. Integer hendrerit congue dui, at tincidunt neque elementum nec.</p>
    <div class="welcome-body">
      <div class="welcome-photo" role="img" aria-label="Builders in hard hats reviewing plans"></div>
      <div class="welcome-aside">
        <p>Lorem ipsum dolor sit amet, consectetur adipiscing elit. Donec vitae metus tempor arcu ultricies mollis ac non erat.</p>
        <ul>
          <li>Lorem ipsum dolor sit amet, consectetur adipiscing elit.</li>
          <li>Donec vitae metus tempor arcu ultricies mollis ac non erat.</li>
          <li>Ut eu erat quis leo imperdiet pellentesque.</li>
        </ul>
      </div>
    </div>
    <p>Lorem ipsum dolor sit amet, consectetur adipiscing elit. Nullam eu urna enim, sit amet venenatis arcu. Proin ultrices rutrum ante, sed cursus leo sollicitudin in. Integer hendrerit congue dui, at tincidunt neque elementum nec.</p>
  </section>

  <aside class="gallery">
    <h2 class="section-title">Our Gallery</h2>
    <div class="gallery-item">
      <div class="gallery-thumb" role="img" aria-label="1:50 scale house model with swimming pool" style="background:linear-gradient(#e9ebe6,#b9c0b0 60%,#6aa0b8)"></div>
      <div><h3>1:50 House<br>Scale Model</h3><p>Swimming pools come out really well and add another realistic element to the visualisation....</p></div>
    </div>
    <div class="gallery-item">
      <div class="gallery-thumb" role="img" aria-label="Detailed 1:50 scale house model" style="background:linear-gradient(#d8d6e0,#b59f9a 55%,#6f8a62)"></div>
      <div><h3>1:50 House<br>Scale Model</h3><p>A lot of detail can be expressed at 1:50 scale....</p></div>
    </div>
    <div class="gallery-item">
      <div class="gallery-thumb" role="img" aria-label="House scale model with landscaped garden" style="background:linear-gradient(#cfd4d8,#9aa39a 55%,#4f6b4a)"></div>
      <div><h3>1:50 House<br>Scale Model</h3><p>House model showing the added level of detail achievable at 1:50 scale...</p></div>
    </div>
  </aside>

  <footer class="site-footer">
    <div class="legal">© Copyright The Brisk Loft<br>Phone: (08) 5550 0147 Australia</div>
    <div class="social" aria-label="Social links"><span></span><span></span><span></span></div>
  </footer>
</div>
</body>
</html>
```